Make my Savory Fungi Strips sell!!

Design for a new mushroom jerky product.
The meatiest (no) beef jerky ever!!
Bite it! Rip it! Tear it! Chew it! There is nothing meatier! Not even meat!
Please use our company logo (supplied) somewhere on the package. It does not have to be the focus. Just anywhere in the design.
Not sure if I want to focus on the plant based, healthy, clean - eating design or a masculine, taste based, BBQ, design. Surprise me!
Will be used on a stand up pouch, with a window.

Target Market(s)

Jerky lovers. Plant based connoisseurs. Vegans. Millenials. People that want a true meat experience without the cruelty.

Requirements
Must have
• Verdant Crest Foods logo.
Nice to have
• Mushrooms, shiitake, nature, muscles, happy cows?,
Should not have
• The word vegan. Stick to Plant Based.

```html
<!DOCTYPE html>
<html lang="en">
<head>
<meta charset="utf-8">
<title>Savory Fungi Strips – Pouch Label</title>
<link href="https://fonts.googleapis.com/css2?family=Alfa+Slab+One&family=Lilita+One&family=Gochi+Hand&display=swap" rel="stylesheet">
<style>
  :root {
    --backdrop: #7b4a4a;
    --label-pink: #f2a2a2;
    --pattern-tone: #e89393;
    --panel-white: #ffffff;
    --ink-brown: #3a2418;
    --jerky-red: #9b3033;
    --tagline-ink: #333333;
    --brand-green: #6fb23a;
    --art-mushroom: #e9cdb0;
    --art-jerky: #c99a94;
  }
  * { margin: 0; padding: 0; box-sizing: border-box; }
  html, body { width: 1200px; height: 1200px; overflow: hidden; }
  body { background: var(--backdrop); position: relative; }

  .label {
    position: absolute;
    left: 227px; top: 40px;
    width: 746px; height: 1120px;
    background: var(--label-pink);
    overflow: hidden;
  }
  .label__pattern {
    position: absolute; inset: 0;
    background: linear-gradient(180deg, var(--label-pink), var(--pattern-tone));
  }
  .label__panel {
    position: absolute;
    left: -16px; top: 250px;
    width: 778px; height: 778px;
    border-radius: 50%;
    background: var(--panel-white);
  }
  .label__band {
    position: absolute;
    left: 0; right: 0; top: 935px; height: 92px;
    background: var(--panel-white);
  }
  .brand__disc {
    position: absolute;
    left: 308px; top: 925px;
    width: 130px; height: 130px;
    border-radius: 50%;
    background: var(--panel-white);
  }

  .label__title {
    position: absolute; left: 0; right: 0; top: 92px;
    text-align: center;
    line-height: 1;
    font-weight: 400;
  }
  .title__line { display: block; white-space: nowrap; }
  .title__line--top { font-size: 86px; }
  .title__line--bottom { font-size: 46px; margin-top: 14px; }
  .title__word {
    -webkit-text-stroke: 12px var(--panel-white);
    paint-order: stroke fill;
  }
  .title__word--dark { font-family: "Alfa Slab One", serif; color: var(--ink-brown); }
  .title__word--red { font-family: "Lilita One", sans-serif; color: var(--jerky-red); }
  .title__line--top .title__word--red { font-size: 92px; letter-spacing: 1px; }
  .title__line--bottom .title__word--red { font-size: 50px; }

  .label__art {
    position: absolute;
    left: 90px; top: 320px;
    width: 540px; height: 390px;
    border-radius: 46% 46% 40% 40%;
    background: linear-gradient(100deg, var(--art-mushroom) 0%, var(--art-mushroom) 48%, var(--art-jerky) 60%, var(--art-jerky) 100%);
    opacity: 0.8;
  }
  .label__tagline {
    position: absolute; left: 0; right: 0; top: 748px;
    text-align: center;
    font-family: "Gochi Hand", cursive;
    font-size: 24px;
    line-height: 1.45;
    color: var(--tagline-ink);
  }

  .brand__mark {
    position: absolute; left: 0; right: 0; top: 976px;
    display: flex; align-items: center; justify-content: center; gap: 8px;
  }
  .brand__dot {
    width: 24px; height: 24px; border-radius: 50%;
    background: var(--brand-green);
  }
  .brand__name {
    font-family: "Gochi Hand", cursive;
    font-size: 24px;
    line-height: 1;
    color: var(--brand-green);
  }
</style>
</head>
<body>
  <main class="label">
    <div class="label__pattern" role="img" aria-label="Repeating pattern of small mushrooms and jerky strips on pink"></div>
    <div class="label__panel"></div>
    <div class="label__band"></div>
    <div class="brand__disc"></div>

    <h1 class="label__title">
      <span class="title__line title__line--top"><span class="title__word title__word--dark">The </span><span class="title__word title__word--red">CHEWIEST</span></span>
      <span class="title__line title__line--bottom"><span class="title__word title__word--red">Savory Fungi Strips </span><span class="title__word title__word--dark">Ever!!</span></span>
    </h1>

    <div class="label__art" role="img" aria-label="Cartoon shiitake mushroom and jerky strip characters dancing arm in arm"></div>

    <p class="label__tagline">Bite it! Rip it! Tear it! Chew it!<br>There is nothing meatier! Not even meat!</p>

    <div class="brand__mark">
      <span class="brand__dot"></span>
      <span class="brand__name">Verdant Crest Foods</span>
    </div>
  </main>
</body>
</html>
```